Larkmont Business Card Design Project

Double side card , just the logo on oxford white background on one side , and the rest of the information on the other side..
the company name is : Larkmont International General Trading LLC.
logo is already attached
the card to show in the info side: company name, employee name and position (job title) phone number, fax number, email address, P.O. box, Location (city and country)
deadline is already extended 4 all to have more time... thanks

```html
<!DOCTYPE html>
<html lang="en">
<head>
<meta charset="utf-8">
<title>Larkmont Business Card Concepts</title>
<link rel="stylesheet" href="https://fonts.googleapis.com/css2?family=Ubuntu:wght@400;500;700&display=swap">
<style>
  :root {
    --stage: #000;
    --ink: #2a2a2a;
    --charcoal: #232323;
    --slate: #2b3039;
    --paper: #fff;
    --mist: #efefef;
    --ice: #dce8ee;
    --cyan: #36c0e0;
    --aqua: #3fe0e0;
    --sky: #2a9be0;
    --royal: #1a5fe0;
    --blue: #2f8fe6;
    --muted: #9aa0a6;
  }
  * { box-sizing: border-box; margin: 0; padding: 0; }
  html, body { width: 1200px; height: 750px; overflow: hidden; background: var(--stage); }
  body { position: relative; font-family: "Ubuntu", sans-serif; }
  .card { position: absolute; overflow: hidden; background: var(--paper); }
  .card > svg.shape { position: absolute; inset: 0; }
  .abs { position: absolute; }
  .wordmark { position: absolute; font-weight: 500; letter-spacing: 2px; white-space: nowrap; }

  /* Card 1 */
  .card--swoosh { left: 22px; top: 20px; width: 554px; height: 332px; }
  .card--swoosh .wordmark { left: 38px; top: 100px; font-size: 27px; color: var(--ink); }
  .card--swoosh .holder { left: 38px; top: 270px; color: #fff; }
  .holder-name { font-size: 19px; font-weight: 700; }
  .holder-role { font-size: 9px; margin-top: 3px; }
  .contact-list { right: 36px; top: 203px; color: #fff; font-size: 10px; text-align: right; }
  .contact-row { display: flex; justify-content: flex-end; align-items: center; gap: 8px; height: 24.5px; }
  .contact-row svg { width: 12px; height: 12px; flex: none; }
  .contact-row .stack { line-height: 16px; }

  /* Card 2 */
  .card--chevron { left: 598px; top: 20px; width: 553px; height: 332px; background: var(--mist); }
  .card--chevron .wordmark { left: 22px; top: 150px; font-size: 23px; color: #fff; }
  .card--chevron .holder { right: 44px; top: 68px; text-align: right; color: #fff; }
  .card--chevron .holder-name { font-size: 17px; }
  .card--chevron .holder-name span { font-weight: 400; }
  .card--chevron .holder-role { font-size: 8px; }
  .company { right: 44px; top: 160px; text-align: right; color: #333; }
  .company-name { font-size: 15px; font-weight: 700; color: var(--cyan); }
  .company-name span { color: #222; font-weight: 500; }
  .company-addr { font-size: 10px; margin-top: 3px; }
  .hex-row { right: 42px; display: flex; align-items: center; gap: 8px; font-size: 10px; color: #333; text-align: right; line-height: 14px; }
  .hex-row svg { width: 30px; height: 30px; flex: none; }
  .hex-row--phone { top: 215px; }
  .hex-row--web { top: 258px; }
  .rule-line { position: absolute; height: 1px; background: linear-gradient(90deg, transparent, var(--cyan)); }

  /* Card 3 */
  .card--tabs { left: 22px; top: 372px; width: 554px; height: 331px; background: var(--charcoal); }
  .card--tabs .holder { left: 52px; top: 78px; color: #fff; }
  .card--tabs .holder-name { font-size: 18px; }
  .card--tabs .holder-role { font-size: 14px; color: var(--aqua); margin-top: 2px; }
  .detail-block { left: 52px; color: #fff; font-size: 14px; line-height: 18px; }
  .detail-block--addr { top: 152px; }
  .detail-block--phone { top: 202px; }
  .detail-block--web { top: 250px; }
  .card--tabs .wordmark { left: 312px; top: 186px; font-size: 26px; color: var(--ink); }

  /* Card 4 */
  .card--bar { left: 595px; top: 372px; width: 558px; height: 321px; }
  .card--bar .wordmark { left: 28px; top: 104px; font-size: 36px; color: var(--ink); }
  .bar-address { left: 17px; top: 217px; font-size: 17px; color: #fff; }
  .card--bar .holder { right: 15px; top: 195px; text-align: right; color: var(--blue); font-size: 20px; line-height: 25px; }
  .card--bar .holder-name { font-size: 20px; }
  .card--bar .holder-role { font-size: 20px; font-weight: 500; margin-top: 0; }
  .bar-contact { top: 262px; color: #fff; font-size: 17px; line-height: 26px; }
  .bar-contact--phone { left: 72px; }
  .bar-contact--mail { left: 293px; }
  .bar-icon { position: absolute; top: 272px; width: 30px; height: 30px; }
</style>
</head>
<body>

<!-- Card 1: swoosh front -->
<section class="card card--swoosh">
  <svg class="shape" width="554" height="332" viewBox="0 0 554 332">
    <defs>
      <linearGradient id="swooshBlue" x1="0" x2="1" y1="0" y2="0">
        <stop offset="0" stop-color="#3fd6e8"/>
        <stop offset="0.5" stop-color="#2b9ee6"/>
        <stop offset="1" stop-color="#1a55e0"/>
      </linearGradient>
    </defs>
    <path d="M0,170 C200,160 380,110 554,55 L554,108 C380,150 200,180 0,186 Z" fill="#eeeeee"/>
    <path d="M0,180 C220,178 400,145 554,104 L554,170 L0,192 Z" fill="url(#swooshBlue)"/>
    <path d="M0,188 L554,160 L554,332 L0,332 Z" fill="#222"/>
  </svg>
  <div class="wordmark">LARKMONT INT.</div>
  <div class="abs holder">
    <div class="holder-name">DANA R. WHITFIELD</div>
    <div class="holder-role">CEO</div>
  </div>
  <div class="abs contact-list">
    <div class="contact-row">+ 417-555-0146
      <svg viewBox="0 0 12 12"><circle cx="6" cy="6" r="5.3" fill="none" stroke="#fff"/><path d="M4,3.3 L5,3 L5.6,4.6 L5,5.1 Q5.6,6.6 6.9,7 L7.4,6.4 L9,7 L8.7,8 Q6.5,8.6 4.6,6.6 Q3.4,5 4,3.3Z" fill="#fff"/></svg>
    </div>
    <div class="contact-row">+ 417-555-0147
      <svg viewBox="0 0 12 12"><rect x="3" y="1.5" width="6" height="3" fill="#fff"/><rect x="1" y="4.5" width="10" height="4.5" rx="1" fill="#fff"/><rect x="3" y="7.5" width="6" height="3.5" fill="#222" stroke="#fff"/></svg>
    </div>
    <div class="contact-row">DanaRWhitfield@corvelane.com
      <svg viewBox="0 0 12 12"><text x="6" y="10" font-size="12" font-family="Ubuntu, sans-serif" fill="#fff" text-anchor="middle">@</text></svg>
    </div>
    <div class="contact-row" style="height:40px"><div class="stack">214 Hollow Pine Road<br>Marston, MO 64720</div>
      <svg viewBox="0 0 12 12"><path d="M6,1 A3.5,3.5 0 0 1 9.5,4.5 C9.5,7 6,11 6,11 C6,11 2.5,7 2.5,4.5 A3.5,3.5 0 0 1 6,1Z" fill="none" stroke="#fff"/><circle cx="6" cy="4.5" r="1.2" fill="#fff"/></svg>
    </div>
  </div>
</section>

<!-- Card 2: chevron back -->
<section class="card card--chevron">
  <svg class="shape" width="553" height="332" viewBox="0 0 553 332">
    <rect x="0" y="0" width="553" height="131" fill="#151515"/>
    <polygon points="0,0 246,0 266,132 160,332 0,332" fill="#fff"/>
    <polygon points="0,0 232,0 252,132 147,332 0,332" fill="#36c0e0"/>
  </svg>
  <div class="wordmark">LARKMONT INT.</div>
  <div class="abs holder">
    <div class="holder-name">DANA R. <span>WHITFIELD</span></div>
    <div class="holder-role">CEO</div>
  </div>
  <div class="abs company">
    <div class="company-name">LARKMONT <span>INT.</span></div>
    <div class="company-addr">214 Hollow Pine Road, Marston, MO 64720</div>
  </div>
  <div class="rule-line" style="left:330px;top:230px;width:150px"></div>
  <div class="rule-line" style="left:330px;top:273px;width:150px"></div>
  <div class="abs hex-row hex-row--phone">
    <div>+123-555-0190<br>(F)+ 1235550192</div>
    <svg viewBox="0 0 30 30"><polygon points="8,2 22,2 29,15 22,28 8,28 1,15" fill="#36c0e0"/><rect x="9" y="13" width="12" height="8" rx="1.5" fill="#fff"/><path d="M8,12 Q15,6 22,12 L20,14 L10,14Z" fill="#fff"/></svg>
  </div>
  <div class="abs hex-row hex-row--web">
    <div>DanaRWhitfield@corvelane.com<br>www.corvelane.com</div>
    <svg viewBox="0 0 30 30"><polygon points="8,2 22,2 29,15 22,28 8,28 1,15" fill="#36c0e0"/><rect x="8" y="9" width="14" height="10" fill="none" stroke="#fff" stroke-width="1.6"/><rect x="11" y="21" width="8" height="1.6" fill="#fff"/></svg>
  </div>
</section>

<!-- Card 3: tabbed split -->
<section class="card card--tabs">
  <svg class="shape" width="554" height="331" viewBox="0 0 554 331">
    <polygon points="228,0 554,0 554,331 313,331" fill="#fff"/>
    <line x1="52" y1="195" x2="258" y2="195" stroke="#444"/>
    <line x1="52" y1="244" x2="278" y2="244" stroke="#444"/>
    <polygon points="218,145 258,145 270,193 230,193" fill="#3fe0e0"/>
    <polygon points="231,196 271,196 283,243 243,243" fill="#2a9be0"/>
    <polygon points="244,246 284,246 296,294 256,294" fill="#1a5fe0"/>
    <path d="M238,172 L245,165 L252,172 M240,170 L240,177 L250,177 L250,170" fill="none" stroke="#fff" stroke-width="2"/>
    <rect x="252" y="217" width="12" height="8" rx="1.5" fill="#fff"/>
    <path d="M251,216 Q258,210 265,216 L263,218 L253,218Z" fill="#fff"/>
    <rect x="266" y="263" width="14" height="10" fill="none" stroke="#fff" stroke-width="2"/>
    <rect x="269" y="275" width="8" height="2" fill="#fff"/>
  </svg>
  <div class="abs holder">
    <div class="holder-name">DANA R. WHITFIELD</div>
    <div class="holder-role">CEO</div>
  </div>
  <div class="abs detail-block detail-block--addr">214 Hollow Pine Road<br>Marston, MO 64720</div>
  <div class="abs detail-block detail-block--phone">(123) 555-0190<br>F: (123) 555-0192</div>
  <div class="abs detail-block detail-block--web">DanaRWhitfield@corvelane.com<br>www.corvelane.com</div>
  <div class="wordmark">LARKMONT INT.</div>
</section>

<!-- Card 4: banded -->
<section class="card card--bar">
  <svg class="shape" width="558" height="321" viewBox="0 0 558 321">
    <polygon points="372,181 558,181 558,251 348,251" fill="#dce8ee"/>
    <polygon points="0,203 360,203 338,251 0,251" fill="#2f8fe6"/>
    <rect x="0" y="251" width="558" height="70" fill="#2b3039"/>
  </svg>
  <div class="wordmark">LARKMONT INT.</div>
  <div class="abs bar-address">214 Hollow Pine Road, Marston, MO 64720</div>
  <div class="abs holder">
    <div class="holder-name">DANA R. WHITFIELD</div>
    <div class="holder-role">CEO</div>
  </div>
  <svg class="bar-icon" style="left:26px" viewBox="0 0 30 30"><circle cx="15" cy="15" r="13" fill="none" stroke="#fff" stroke-width="2"/><path d="M10,8 L12.5,7.5 L14,11.5 L12.5,13 Q14,16.5 17,17.5 L18.5,16 L22.5,17.5 L22,20 Q16.5,21.5 12,17 Q8.8,13 10,8Z" fill="#fff"/></svg>
  <div class="abs bar-contact bar-contact--phone">+ 417-555-0146<br>+ 417-555-0147(F)</div>
  <svg class="bar-icon" style="left:242px" viewBox="0 0 30 30"><text x="15" y="25" font-size="30" font-family="Ubuntu, sans-serif" fill="#fff" text-anchor="middle">@</text></svg>
  <div class="abs bar-contact bar-contact--mail">DanaRWhitfield@corvelane.com<br>www.corvelane.com</div>
</section>

</body>
</html>
```